Customizable Form Generation Website

This will be a place for users to quickly generate numerous forms from a categorized list. As the forms are templates with field variables, the site must be able to substitute ‘real data’ for template variable data. This tool will allow for quick custom forms on-demand.

The landing page is attached. We need the User Experience and User Interface solved for us.

EXAMPLE:
——————————————————————-
Dear {{PatientFirstName}},

Please come back for an examination on {{SelectedDate}} with Doctor {{SelectedProvider}}.

Sincerely,

{{SelectedAuthor}}
——————————————————————-

Coming to the Forms Landing Page, the user will see the forms available to select. The user will then click to select a form.

At some point, the user must resolve the variables in the form. For instance, there are the following variables in the above example: PatientFirstName, SelectedDate, SelectedProvider, and SelectedAuthor. We must give the user a chance to select the values for these variables. Using a dropdown combobox will probably work for most. Getting a date selector will be required if the variable happens to contain the string 'date'.

Is it best to preselect common variables before opening the form, or is it best to dynamically scan the template, then give the user the option to give values to each variable found?

The design must include a way for users to upload additional forms. Forms will most probably be PDF, .DOC, .TXT files. This allows users to develop simple or fancy forms of their choosing., then simply drop them into the site for future use.

The design must include a way for users to create new forms. The form creation tool must present to the user the list of predefined variables like {{PatientLastName}} for easy insertion into the form writer. Anytime "{{}}" are used, developers will recognize that as a variable that needs to be resolved.

The forms will be separated into categories as follows:

OFFICE:
- Letterhead
- Sign-In Sheet
- Fax Cover Sheet
SCHEDULER:
- Appointment Reminder
- Missed Appointment Policy
PATIENT:
- Intake Form
- Patient Discharge
- Return to Work or School
- Excuse Slip
- Consent to Treat a Minor
- Verify Non-Pregnancy
RELEASE:
- Health Information Release Form
- X-Ray Release Form
CERTIFICATES:
- Certificate of Care
- Disability Certificate
INSURANCE:
- Authorization to Bill Insurance
- Assignment Authorization
OTHER:
- Free Massage
- Free Vitamins

The design must include a way to add/customize categories. Categories are for organizing the forms logically.

We welcome ANY questions to help understand the requirements.

Good luck!

Industry/Entity Type

Healthcare

Number of Pages Required

3 page

Requirements
Must have
• Must Follow VELLUM PATTERN standards
Nice to have
• Great User Experience. Simple, Fast, Clever.
Should not have
• nothing to add here

```html
<!DOCTYPE html>
<html lang="en">
<head>
<meta charset="utf-8">
<title>ClinicDesk – Forms</title>
<link href="https://fonts.googleapis.com/css2?family=Montserrat:wght@400;500;600;700&family=Great+Vibes&display=swap" rel="stylesheet">
<style>
:root{
  --stage:#767676;
  --sidebar:#053a5e;
  --sidebar-active:#0a6d99;
  --sidebar-line:#14507a;
  --header:#011b2b;
  --content:#eceef9;
  --card:#ffffff;
  --orange:#ff6a00;
  --ink:#111318;
  --muted:#444;
  --tile:#e9eaee;
}
*{box-sizing:border-box;margin:0;padding:0}
html,body{width:872px;height:1200px;overflow:hidden}
body{background:var(--stage);font-family:"Montserrat",sans-serif;color:var(--ink);position:relative}
.screen{position:absolute;left:70px;width:731px;height:524px;background:var(--content);box-shadow:0 10px 40px rgba(0,0,0,.45);overflow:hidden}
.screen--compose{top:61px}
.screen--library{top:615px}
.sidebar{position:absolute;left:0;top:0;width:88px;height:100%;background:var(--sidebar)}
.nav{list-style:none}
.nav li{height:46px;display:flex;align-items:center;color:#fff;font-size:8.3px;font-weight:500;padding-left:17px;position:relative}
.nav li:first-child{height:55px;padding-top:9px}
.nav li.line::after{content:"";position:absolute;left:7px;right:6px;bottom:0;height:1px;background:var(--sidebar-line)}
.nav li.active{background:var(--sidebar-active)}
.nav svg{width:11px;height:11px;margin-right:11px;fill:#fff;flex:none}
.topbar{position:absolute;left:88px;top:0;right:0;height:60px;background:var(--header);color:#fff}
.brand{position:absolute;left:16px;top:20px;display:flex;align-items:center;gap:7px;font-size:16px;font-weight:700;color:#fff}
.brand .dot{width:19px;height:19px;border:2px solid var(--orange);border-radius:50%}
.practice{position:absolute;left:296px;top:23px;font-size:11px;display:flex;align-items:center;gap:7px}
.practice svg{width:9px;height:11px;fill:var(--orange)}
.welcome{position:absolute;right:102px;top:13px;text-align:right;line-height:1.2}
.welcome small{font-size:7.5px;display:block}
.welcome b{font-size:11px;font-weight:700}
.avatar{position:absolute;right:64px;top:15px;width:31px;height:31px;border-radius:50%;background:radial-gradient(circle at 50% 40%,#c89a7e,#5b4336)}
.logout{position:absolute;right:11px;top:18px;width:18px;height:16px}
.card{position:absolute;left:100px;top:72px;width:620px;background:var(--card);border-radius:3px;box-shadow:0 1px 3px rgba(0,0,0,.08)}
.footer{position:absolute;left:88px;right:0;top:481px;text-align:center;font-size:8.4px;color:#222}
.footer span{margin:0 5px}
/* compose letter */
.letter{height:370px;padding:0 32px}
.letter h1{position:absolute;left:65px;top:38px;font-size:19px;font-weight:700}
.burger{position:absolute;left:32px;top:42px;width:18px;height:15px}
.greet{position:absolute;left:33px;top:101px;font-size:13.5px;font-weight:700}
.field-label{position:absolute;left:33px;font-size:9.3px;font-weight:500}
.field{position:absolute;left:249px;width:183px;height:32px;border:1px solid #c9c9c9;border-radius:2px}
.field svg{position:absolute;right:10px;top:11px;width:9px;height:9px}
.signoff{position:absolute;left:33px;top:264px;font-size:18px;font-weight:500}
.author{position:absolute;left:33px;top:296px;font-family:"Great Vibes",cursive;font-size:28px;color:#777}
/* library */
.library{height:371px}
.tabs{position:absolute;left:14px;top:20px;display:flex;gap:4px}
.tab{width:81px;height:70px;border:2px solid var(--orange);display:flex;flex-direction:column;align-items:center;justify-content:flex-end;padding-bottom:9px;font-size:7.8px;font-weight:700;color:var(--ink);position:relative}
.tab svg{width:20px;height:22px;fill:var(--orange);position:absolute;top:10px}
.tab.active{background:var(--orange);color:#fff}
.tab.active svg{fill:#fff}
.tab.active::after{content:"";position:absolute;bottom:-8px;left:50%;margin-left:-6px;border:6px solid transparent;border-top-color:var(--orange);border-bottom:0}
.forms{position:absolute;left:16px;top:122px;display:flex;gap:10px}
.form-tile{width:189px;height:207px;background:var(--tile);border-radius:4px;position:relative}
.form-tile h2{text-align:center;font-size:13.5px;font-weight:700;padding-top:34px}
.preview{position:absolute}
</style>
</head>
<body>
<svg width="0" height="0" style="position:absolute">
  <symbol id="i-home" viewBox="0 0 12 12"><path d="M6 1 0 6h2v5h3V8h2v3h3V6h2z"/></symbol>
  <symbol id="i-cal" viewBox="0 0 12 12"><path d="M1 2h10v10H1zM3 0h1v3H3zm5 0h1v3H8zM2 5v6h8V5z"/><path d="M3 6h2v2H3zm4 0h2v2H7zM3 9h2v1H3z"/></symbol>
  <symbol id="i-users" viewBox="0 0 12 12"><circle cx="6" cy="3.5" r="2"/><circle cx="2.5" cy="4" r="1.5"/><circle cx="9.5" cy="4" r="1.5"/><path d="M2.5 11c0-3 1.5-5 3.5-5s3.5 2 3.5 5zM0 9c0-2 1-3 2.5-3L2 9zm12 0c0-2-1-3-2.5-3L10 9z"/></symbol>
  <symbol id="i-undo" viewBox="0 0 12 12"><path d="M6 1a5 5 0 1 1-5 5h2a3 3 0 1 0 3-3v2L2 2 6-1z"/></symbol>
  <symbol id="i-card" viewBox="0 0 12 12"><path d="M0 2h12v9H0zm1 1v1h10V3zm0 3v4h10V6zm1 2h3v1H2z"/></symbol>
  <symbol id="i-doc" viewBox="0 0 12 12"><path d="M2 0h5l3 3v9H2zm1 1v10h6V4H6V1zm1 5h4v1H4zm0 2h4v1H4z"/></symbol>
  <symbol id="i-chart" viewBox="0 0 12 12"><path d="M0 1h1v10h11v1H0z"/><path d="M2 9l3-4 2 2 4-5 .8.6L7 8.4 5 6.5 2.8 9.6z"/></symbol>
  <symbol id="i-mega" viewBox="0 0 12 12"><path d="M1 4h3l6-3v10L4 8H1zM3 8h2l1 3H4z"/></symbol>
  <symbol id="i-forms" viewBox="0 0 12 12"><path d="M4 0h7v8H8v4H1V4h3zm1 1v3h3v3h2V1zM2 5v6h5V5z"/></symbol>
  <symbol id="i-list" viewBox="0 0 12 12"><path d="M0 2h12v2H0zm0 3h12v2H0zm0 3h12v2H0z"/></symbol>
  <symbol id="i-user" viewBox="0 0 12 12"><circle cx="6" cy="3.5" r="3"/><path d="M1 12c0-4 2-5.5 5-5.5s5 1.5 5 5.5z"/></symbol>
  <symbol id="i-building" viewBox="0 0 10 12"><path d="M0 0h10v12H6V9H4v3H0zm2 2v2h2V2zm4 0v2h2V2zM2 5v2h2V5zm4 0v2h2V5z"/></symbol>
  <symbol id="i-logout" viewBox="0 0 18 16"><path d="M7 1H2v14h5" fill="none" stroke="#fff" stroke-width="2"/><path d="M8 5h5V1l5 7-5 7v-4H8z" fill="#fff"/></symbol>
</svg>

<!-- Compose screen -->
<section class="screen screen--compose">
  <aside class="sidebar">
    <ul class="nav">
      <li class="line"><svg><use href="#i-home"/></svg>Home</li>
      <li class="line"><svg><use href="#i-cal"/></svg>Scheduler</li>
      <li class="line"><svg><use href="#i-users"/></svg>Patients</li>
      <li class="line"><svg><use href="#i-undo"/></svg>Encounters</li>
      <li class="line"><svg><use href="#i-card"/></svg>Payments</li>
      <li class="line"><svg><use href="#i-doc"/></svg>Billing</li>
      <li><svg><use href="#i-chart"/></svg>Reporting</li>
      <li><svg><use href="#i-mega"/></svg>Marketing</li>
      <li class="active"><svg><use href="#i-forms"/></svg>Forms</li>
      <li><svg><use href="#i-list"/></svg>Lists</li>
      <li><svg><use href="#i-user"/></svg>Admin</li>
    </ul>
  </aside>
  <header class="topbar">
    <div class="brand"><span class="dot"></span>ClinicDesk</div>
    <div class="practice"><svg><use href="#i-building"/></svg>Sample healthcare practice</div>
    <div class="welcome"><small>Welcome</small><b>Back,Test</b></div>
    <div class="avatar" role="img" aria-label="User profile photo"></div>
    <svg class="logout"><use href="#i-logout"/></svg>
  </header>
  <main class="card letter">
    <svg class="burger" viewBox="0 0 18 15"><path d="M0 0h18v3H0zm0 6h18v3H0zm0 6h18v3H0z" fill="#ff6a00"/></svg>
    <h1>Forms</h1>
    <p class="greet">Dear John</p>
    <p class="field-label" style="top:146px">Please come back for an examination on</p>
    <div class="field" style="top:136px"><svg viewBox="0 0 12 12"><use href="#i-cal" fill="#111"/></svg></div>
    <p class="field-label" style="top:195px">With Doctor</p>
    <div class="field" style="top:185px"><svg viewBox="0 0 10 10"><path d="M1 3l4 4 4-4" fill="none" stroke="#111" stroke-width="1.8"/></svg></div>
    <p class="signoff">Sincerely,</p>
    <p class="author">Author Name</p>
  </main>
  <footer class="footer">(c)2021 Companyname.All Rights Reserved<span>|</span>Privacy Policy<span>|</span>Terms and Use</footer>
</section>

<!-- Library screen -->
<section class="screen screen--library">
  <aside class="sidebar">
    <ul class="nav">
      <li class="active"><svg><use href="#i-home"/></svg>Home</li>
      <li class="line"><svg><use href="#i-cal"/></svg>Scheduler</li>
      <li class="line"><svg><use href="#i-users"/></svg>Patients</li>
      <li class="line"><svg><use href="#i-undo"/></svg>Encounters</li>
      <li class="line"><svg><use href="#i-card"/></svg>Payments</li>
      <li class="line"><svg><use href="#i-doc"/></svg>Billing</li>
      <li><svg><use href="#i-chart"/></svg>Reporting</li>
      <li><svg><use href="#i-mega"/></svg>Marketing</li>
      <li><svg><use href="#i-forms"/></svg>Forms</li>
      <li><svg><use href="#i-list"/></svg>Lists</li>
      <li><svg><use href="#i-user"/></svg>Admin</li>
    </ul>
  </aside>
  <header class="topbar">
    <div class="brand"><span class="dot"></span>ClinicDesk</div>
    <div class="practice"><svg><use href="#i-building"/></svg>Sample healthcare practice</div>
    <div class="welcome"><small>Welcome</small><b>Back,Test</b></div>
    <div class="avatar" role="img" aria-label="User profile photo"></div>
    <svg class="logout"><use href="#i-logout"/></svg>
  </header>
  <main class="card library">
    <nav class="tabs">
      <div class="tab active"><svg viewBox="0 0 20 22"><path d="M2 0h16v22h-6v-4H8v4H2zm3 3v2h2V3zm4 0v2h2V3zm4 0v2h2V3zM5 7v2h2V7zm4 0v2h2V7zm4 0v2h2V7zM5 11v2h2v-2zm4 0v2h2v-2zm4 0v2h2v-2z"/></svg>OFFICE</div>
      <div class="tab"><svg viewBox="0 0 20 22"><path d="M1 3h18v19H1zm2 6v11h14V9zM5 0h2v5H5zm8 0h2v5h-2z"/><path d="M6 14l2-2 2 2 4-4 2 2-6 6z"/></svg>SCHEDULER</div>
      <div class="tab"><svg viewBox="0 0 22 22"><path d="M11 0a11 11 0 1 1 0 22 11 11 0 0 1 0-22zm0 2a9 9 0 0 0-6.5 15.2C6 15 8.3 14 11 14s5 1 6.5 3.2A9 9 0 0 0 11 2zm0 2.5a4 4 0 1 1 0 8 4 4 0 0 1 0-8zm0 2a2 2 0 1 0 0 4 2 2 0 0 0 0-4z"/></svg>PATIENT</div>
      <div class="tab"><svg viewBox="0 0 26 20"><path d="M3 1h23v18H1V5h2zm2 2v14h19V3zm2 2h7v6H7zm9 0h6v2h-6zm0 4h6v2h-6zM7 13h15v2H7z"/></svg>RELEASE</div>
      <div class="tab"><svg viewBox="0 0 22 22"><path d="M11 0l2.5 3 3.8-1 .6 3.9 3.8 1.3-1.6 3.6 2 3.3-3.6 1.7-.5 3.9-3.9-.6L11 22l-2.6-2.9-3.9.6-.5-3.9-3.6-1.7 2-3.3L.8 7.2l3.8-1.3.6-3.9 3.8 1z"/></svg>CERTIFICATES</div>
      <div class="tab"><svg viewBox="0 0 20 22"><path d="M1 1h18v9c0 6-4 10-9 12C5 20 1 16 1 10zm3 3v6c0 4 2.5 7 6 8.6V4z"/></svg>INSURANCE</div>
      <div class="tab"><svg viewBox="0 0 24 20"><path d="M0 0h24v3H0zm10 5h14v3H10zm0 5h14v3H10zM0 17h24v3H0zM7 5v8L1 9z"/></svg>OTHER</div>
    </nav>
    <div class="forms">
      <article class="form-tile">
        <h2>Letterhead</h2>
        <div class="preview" role="img" aria-label="Letterhead template preview, navy and gold page" style="left:17px;top:78px;width:68px;height:96px;background:linear-gradient(180deg,#1b1f4b 0 12%,#fff 12% 88%,#1b1f4b 88%);box-shadow:0 2px 4px rgba(0,0,0,.3)"></div>
        <div class="preview" role="img" aria-label="Letterhead template preview, alternate layout" style="left:105px;top:78px;width:68px;height:96px;background:linear-gradient(180deg,#1b1f4b 0 14%,#fff 14% 86%,#1b1f4b 86%);box-shadow:0 2px 4px rgba(0,0,0,.3)"></div>
      </article>
      <article class="form-tile">
        <h2>Sign-In Sheet</h2>
        <div class="preview" role="img" aria-label="Lined sign-in sheet preview" style="left:9px;top:75px;width:79px;height:112px;background:repeating-linear-gradient(180deg,#fff 0 5px,#d6d8dc 5px 6px)"></div>
        <div class="preview" role="img" aria-label="Blank notepad page preview" style="left:99px;top:75px;width:79px;height:112px;background:linear-gradient(135deg,#fafbfc,#eef0f3)"></div>
      </article>
      <article class="form-tile">
        <h2>Fax Cover Sheet</h2>
        <div class="preview" role="img" aria-label="Fax cover sheet preview with yellow accent on dark background" style="left:11px;top:71px;width:168px;height:117px;background:radial-gradient(ellipse at 55% 50%,#e9e7df 0 30%,#2a323a 31%)"></div>
      </article>
    </div>
  </main>
  <footer class="footer">(c)2021 Companyname.All Rights Reserved<span>|</span>Privacy Policy<span>|</span>Terms and Use</footer>
</section>
</body>
</html>
```